Lanternfield Billboard - Financial Services Company (Investments, Tax Planning and Insurance)

Our new office has a billboard directly above the office building. We'd like something eye-catching with a strong Call to Action, with the main part of the billboard being under 7 words if possible. We'd like you to include a way to get ahold of us (either our website lanternfieldllc.example or our phone number 302-418-2967. You may also include in small font something to indicate that we've been serving the area since 1980 (the DE area, the tri-state area, the Copperleaf Basin, etc.)

We offer financial planning, tax planning, and insurance, and we help our clients to focus on their goals and happiness by providing everything they need for lifelong wealth under one roof.

Our logos are attached, we use a triangle logo with green and gray. We use the tagline "experience lifelong wealth" but this does not need to be included.

Potential ideas we have seen from other financial companies-
- the concept that the driver spends more time looking at billboards than planning for their retirement
-something along the lines of "everything you need for your finances is in this building right here" planning, investments, taxes, insurance"
-don't spend your time worrying about retirement, let us help you plan for it
-are you working for your money, or is it working for you?
- retirement takes planning, we're here to help
- ready to retire? talk to us
- need investment advice?
- need help investing?
- crossing your fingers isn't a retirement plan. we can help.
- retiring soon? you need help.

Those are just general ideas, please feel free to be creative.

brand colors:
#00b585
#00b185
#000000
#ffffff
#6d6f75
#6d6f75
#6f7074
#021712
#052e24

```html
<!DOCTYPE html>
<html lang="en">
<head>
<meta charset="utf-8">
<title>Lanternfield Billboard</title>
<link rel="stylesheet" href="https://fonts.googleapis.com/css2?family=League+Spartan:wght@400;500;700;800&display=swap">
<style>
  :root {
    --green: #00b585;
    --green-mid: #1fa57a;
    --green-deep: #052e24;
    --green-ink: #021712;
    --gray: #6d6f75;
    --white: #ffffff;
    --page: #eef0ef;
  }
  html, body {
    margin: 0;
    width: 952px;
    height: 1200px;
    overflow: hidden;
    background: var(--page);
    font-family: "League Spartan", sans-serif;
  }
  .canvas {
    position: relative;
    width: 952px;
    height: 1200px;
  }
  .billboard {
    position: absolute;
    left: 0;
    top: 366px;
    width: 952px;
    height: 468px;
    overflow: hidden;
    background: linear-gradient(90deg, #14a373 0%, #2fb78c 25%, #8fd3bd 40%, #e9f4f0 55%, #f7f8f8 70%, #ffffff 100%);
  }
  .photo {
    position: absolute;
    left: 310px;
    top: 0;
    width: 642px;
    height: 468px;
    background:
      linear-gradient(180deg, rgba(255,255,255,.25) 0%, rgba(255,255,255,0) 40%, rgba(255,255,255,.6) 100%),
      linear-gradient(90deg,
        rgba(120,150,130,0) 0%,
        rgba(120,150,130,.45) 18%,
        rgba(110,135,120,.5) 38%,
        rgba(225,230,228,.6) 52%,
        rgba(170,185,205,.45) 64%,
        rgba(215,200,185,.5) 78%,
        rgba(240,236,232,.3) 100%);
  }
  .art {
    position: absolute;
    inset: 0;
  }
  .headline {
    position: absolute;
    left: 42px;
    top: 42px;
    margin: 0;
    text-transform: uppercase;
    line-height: 1;
  }
  .headline span { display: block; }
  .headline .strong-dark  { font-weight: 800; font-size: 54px; color: var(--green-ink); letter-spacing: .5px; }
  .headline .light-dark   { font-weight: 500; font-size: 44px; color: var(--green-ink); margin-top: 4px; }
  .headline .strong-light { font-weight: 800; font-size: 52px; color: var(--white); margin-top: 4px; }
  .headline .light-light  { font-weight: 500; font-size: 44px; color: var(--white); margin-top: 4px; }
  .since-badge {
    position: absolute;
    left: 44px;
    top: 266px;
    width: 100px;
    height: 100px;
    border-radius: 50%;
    background: radial-gradient(circle at 40% 35%, #1b8a66, var(--green-deep));
    box-shadow: 0 4px 10px rgba(0,0,0,.3);
    color: var(--white);
    display: flex;
    flex-direction: column;
    align-items: center;
    justify-content: center;
    transform: rotate(-12deg);
    line-height: .9;
  }
  .since-badge .word { font-size: 21px; font-weight: 500; }
  .since-badge .year { font-size: 28px; font-weight: 700; }
  .contact {
    position: absolute;
    top: 421px;
    display: flex;
    align-items: center;
    gap: 10px;
    color: var(--white);
    font-weight: 700;
    font-size: 20px;
    letter-spacing: 4px;
  }
  .contact.phone { left: 42px; }
  .contact.web { left: 302px; font-size: 19px; letter-spacing: 2.4px; }
  .contact svg { width: 26px; height: 26px; flex: none; }
  .brand {
    position: absolute;
    right: 30px;
    top: 402px;
    display: flex;
    align-items: center;
    gap: 10px;
  }
  .brand .mark {
    width: 22px;
    height: 22px;
    background: var(--green-mid);
  }
  .brand .name {
    font-weight: 700;
    font-size: 38px;
    color: #12905f;
    line-height: 1;
  }
</style>
</head>
<body>
<main class="canvas">
  <section class="billboard">
    <div class="photo" role="img" aria-label="Photo of a smiling senior couple at a desk with a laptop and calculator, talking with a financial advisor"></div>

    <svg class="art" viewBox="0 0 952 468" aria-hidden="true">
      <defs>
        <linearGradient id="bandDark" x1="0" y1="0" x2="1" y2="0">
          <stop offset="0" stop-color="#052e24"/>
          <stop offset=".45" stop-color="#0a5039"/>
          <stop offset=".78" stop-color="#0e6147"/>
          <stop offset=".88" stop-color="#2a7a5f" stop-opacity=".7"/>
          <stop offset="1" stop-color="#ffffff" stop-opacity="0"/>
        </linearGradient>
        <linearGradient id="wedge" x1="0" y1="0" x2="1" y2="0">
          <stop offset="0" stop-color="#00a874" stop-opacity=".35"/>
          <stop offset="1" stop-color="#009a5e" stop-opacity=".9"/>
        </linearGradient>
      </defs>
      <polygon class="corner-wedge" points="952,0 952,150 730,468 725,468" fill="url(#wedge)"/>
      <polygon class="corner-tip" points="900,0 952,0 952,95" fill="#0b9a55"/>
      <path class="swoosh" d="M0 330 C 180 368, 420 388, 952 380 L952 468 L0 468 Z" fill="#ffffff"/>
      <path class="bottom-band" d="M0 350 C 200 388, 420 400, 800 396 L800 468 L0 468 Z" fill="url(#bandDark)"/>
    </svg>

    <h1 class="headline">
      <span class="strong-dark">Retirement</span>
      <span class="light-dark">takes planning,</span>
      <span class="strong-light">we're here</span>
      <span class="light-light">to help</span>
    </h1>

    <div class="since-badge">
      <span class="word">SINCE</span>
      <span class="year">1980</span>
    </div>

    <div class="contact phone">
      <svg viewBox="0 0 26 26" aria-hidden="true">
        <circle cx="13" cy="13" r="11.5" fill="none" stroke="#fff" stroke-width="2"/>
        <path d="M9.2 7.5c.5-.4 1.1-.3 1.4.2l1.1 2c.3.5.1 1-.3 1.3l-.6.4c.5 1.5 1.7 2.8 3.2 3.4l.4-.6c.3-.4.9-.6 1.3-.3l2 1.1c.5.3.6.9.2 1.4l-.9 1c-.6.6-1.5.8-2.3.4-3.1-1.3-5.5-3.7-6.7-6.8-.3-.8-.1-1.700.5-2.3z" fill="#fff"/>
      </svg>
      <span>302-418-2967</span>
    </div>

    <div class="contact web">
      <svg viewBox="0 0 26 26" aria-hidden="true" fill="none" stroke="#fff" stroke-width="1.6">
        <circle cx="13" cy="13" r="11.5" stroke-width="2"/>
        <circle cx="13" cy="13" r="6.5"/>
        <ellipse cx="13" cy="13" rx="2.8" ry="6.5"/>
        <line x1="6.5" y1="13" x2="19.5" y2="13"/>
      </svg>
      <span>lanternfieldllc.example</span>
    </div>

    <div class="brand">
      <span class="mark"></span>
      <span class="name">Lanternfield</span>
    </div>
  </section>
</main>
</body>
</html>
```